Contemporary new French wine brand needs logo and series of label design

to design a new contemporary logo and series of labels for a new French wine brand. We hope to attract not just current French wine drinkers but new ones who may appreciate a less traditional and more modern style.
Updates

Reason: we are wanting to extend the project for a few days more to receive more submissions since we had fewer designs submitted than we were expecting, maybe because of the holidays.

Target Market(s)

people who follow the arts community (eg. music, theatre, visual/video arts, dance) --- all mature ages.

Industry/Entity Type

French Wine

Requirements
Must have
• a clear, memorable treatment for the name CLAVINE with accompanying logo.
Nice to have
• embossing, matte/gloss refinement, tasteful foil stamping, coated stock for the whites to help the integrity of the paper in and out of ice buckets. A combo of say, three types of fonts; a semi custom font for the brand name Clavine and maybe a script and one other.
Should not have
• not traditional French

```html
<!DOCTYPE html>
<html lang="en">
<head>
<meta charset="utf-8">
<title>Clavine – Cabernet Franc Label</title>
<link rel="stylesheet" href="https://fonts.googleapis.com/css2?family=Great+Vibes&display=swap">
<style>
  :root {
    --canvas: #ffffff;
    --panel-top: #0a0001;
    --panel-mid: #2a0012;
    --panel-bottom: #600042;
    --varietal-red: #ec1c24;
    --gold: #c9a46a;
    --ink-light: #ffffff;
  }
  html, body {
    margin: 0;
    padding: 0;
    width: 1200px;
    height: 709px;
    overflow: hidden;
    background: var(--canvas);
  }
  .label {
    position: relative;
    width: 1200px;
    height: 709px;
  }
  .varietal-panel {
    position: absolute;
    left: 128px;
    top: 184px;
    width: 660px;
    height: 525px;
    background: var(--varietal-red);
    border-radius: 0 120px 0 104px;
  }
  .brand-panel {
    position: absolute;
    left: 0;
    top: 0;
    width: 580px;
    height: 578px;
    background: linear-gradient(180deg, var(--panel-top) 0%, var(--panel-mid) 45%, var(--panel-bottom) 100%);
    border-radius: 0 120px 0 128px;
  }
  .brand-name {
    position: absolute;
    left: 56px;
    top: 28px;
    margin: 0;
    font-family: "Great Vibes", cursive;
    font-weight: 400;
    font-size: 132px;
    line-height: 1.2;
    color: var(--gold);
  }
  .vine-illustration {
    position: absolute;
    left: 176px;
    top: 196px;
    width: 368px;
    height: 380px;
    border-radius: 46% 50% 40% 48%;
    background: radial-gradient(ellipse at 55% 50%, rgba(255,255,255,0.22) 0%, rgba(255,255,255,0.08) 55%, rgba(255,255,255,0) 75%);
  }
  .varietal-name {
    position: absolute;
    left: 204px;
    top: 586px;
    margin: 0;
    font-family: "Great Vibes", cursive;
    font-weight: 400;
    font-size: 80px;
    line-height: 1.2;
    color: var(--ink-light);
    white-space: nowrap;
  }
</style>
</head>
<body>
  <main class="label">
    <div class="varietal-panel"></div>
    <div class="brand-panel">
      <h1 class="brand-name">Clavine</h1>
      <div class="vine-illustration" role="img" aria-label="White line illustration of a grape cluster with vine leaves and curling tendrils"></div>
    </div>
    <p class="varietal-name">Cabernet Franc</p>
  </main>
</body>
</html>
```